Ledgerwise Reach - B2B Demand Generation Website Project

We need a fully functional website for www.ledgerwisereach.example. We are a B2B Demand Generation company, based in London, working with companies such as QRT, VKD, Norvex, Brindlow, Tarvo generating them sales leads for their sales teams. We run this through digital marketing newsletter promotions and have a network of websites. Content syndication, data, demand generation, online marketing. Our logo has just been redone (attached) and we have a holding page already which i would like to use the style / colours. Our logo is bright and vibrant but i dont want the site to be a rainbow. We are expensive, classy, professorial, B2B, intelligent.

Home
About Us
Our Services
Prospora & QA Technology
Intent Data
Testimonials
Contact Us
Updates

Target Market(s)

B2B Marketers (QRT, Velquarion, Tarvo, VKD, Opal Reach, Driftmoor, Harlow Quantis, Technology Companies, Data Companies, Marketing Teams, Tumbleden.

Industry/Entity Type

Marketing

Coding

Coded - Design and coding required

Number of Pages Required

5+ page

Font styles to use
Sans Serif

Requirements
Must have
• Home
About Us
Our Services
Prospora & QA Technology
Intent Data
Testimonials
Contact Us

Simple Pages.

Look classy, intelligent, data experts. I like the video homepages were the image moves at the top. Very soft animation.
Nice to have
• Websites i like:

https://www.vkd.example/
https://www.brevantor.example/
https://www.plumfieldsites.example.co.uk/

Ledgerwise Reach - The Demand Generation Company
Should not have
• Glimpsevault crap images

```html
<!DOCTYPE html>
<html lang="en">
<head>
<meta charset="utf-8">
<title>Ledgerwise Reach - The Demand Generation Company</title>
<link rel="stylesheet" href="https://fonts.googleapis.com/css2?family=Kaushan+Script&family=Lato:ital,wght@0,400;0,700;1,400&family=Rubik:wght@400;500;700;900&display=swap">
<style>
:root{
  --navy:#1b3f76;
  --navy-deep:#14315e;
  --navy-btn:#1d4a8a;
  --red:#d2331f;
  --orange:#e2531c;
  --ink:#1d1d1d;
  --text:#6f6f6f;
  --soft:#f5f5f5;
  --line:#e4e4e4;
  --sky:#1c8ad0;
  --white:#ffffff;
}
*{box-sizing:border-box;margin:0;padding:0}
html,body{width:1200px;height:4360px;overflow:hidden}
body{font-family:"Lato",sans-serif;color:var(--text);background:var(--white)}
.page{position:relative;width:1200px;height:4360px;overflow:hidden}
section,header,footer{position:absolute;left:0;width:1200px}
.abs{position:absolute}
.heading{font-family:"Rubik",sans-serif;font-weight:500;color:var(--ink)}
.fill-red{fill:var(--red)}
.fill-white{fill:var(--white)}
.fill-navy{fill:var(--navy)}
.stroke-white{stroke:var(--white)}
.btn{position:absolute;display:flex;align-items:center;justify-content:center;border-radius:22px;font-family:"Rubik",sans-serif;font-size:12px;font-weight:500;color:var(--white);letter-spacing:.2px}
.btn-red{background:var(--red)}
.btn-navy{background:var(--navy-btn)}
.btn-white{background:var(--white);color:var(--ink)}

/* hero */
.hero{top:0;height:675px;background:linear-gradient(160deg,#214a88 0%,var(--navy) 45%,var(--navy-deep) 100%);z-index:2}
.hero-art{position:absolute;left:0;top:0;overflow:visible}
.brand{position:absolute;left:161px;top:24px;display:flex;align-items:center;gap:8px}
.brand-dot{width:30px;height:30px;border-radius:50%;background:var(--red)}
.brand-name{font-family:"Rubik",sans-serif;font-weight:500;font-size:19px;color:var(--orange)}
.brand-tag{position:absolute;left:199px;top:58px;font-size:7.5px;color:#c9d3e4}
.main-nav{position:absolute;left:414px;top:52px;display:flex;gap:24px;font-size:11px;color:#dfe6f2}
.main-nav .active{color:var(--orange);position:relative}
.main-nav .active::after{content:"";position:absolute;left:50%;top:18px;margin-left:-4px;border:4px solid transparent;border-bottom:6px solid var(--orange)}
.search-btn{position:absolute;left:1000px;top:41px;width:38px;height:38px;border-radius:50%;background:var(--red);display:flex;align-items:center;justify-content:center}
.hero-title{position:absolute;left:161px;top:255px;font-family:"Rubik",sans-serif;font-weight:900;font-size:54px;line-height:58px;color:var(--orange);letter-spacing:1px}
.hero-sub{position:absolute;left:161px;top:390px;font-family:"Rubik",sans-serif;font-weight:500;font-size:25px;line-height:30px;color:var(--white)}

/* partners */
.partners{top:675px;height:623px;background:var(--white);z-index:1}
.who-title{position:absolute;left:665px;top:100px;font-family:"Kaushan Script",cursive;font-size:32px;color:var(--ink)}
.step{position:absolute;left:663px;display:flex;gap:24px}
.step-num{width:36px;height:36px;border-radius:50%;background:var(--white);box-shadow:0 2px 6px rgba(0,0,0,.18);display:flex;align-items:center;justify-content:center;font-family:"Rubik",sans-serif;font-size:16px;color:var(--red)}
.step-label{font-size:13px;color:#444;margin-top:2px}
.step-ticker{font-size:11px;font-style:italic;color:var(--sky);margin-top:4px}
.step-link{position:absolute;left:680px;width:2px;height:20px;background:var(--navy)}
.client-row{position:absolute;left:166px;top:468px;display:flex;gap:10px}
.client-box{width:136px;height:56px;border:1px solid var(--line);display:flex;align-items:center;justify-content:center;font-family:"Rubik",sans-serif;font-weight:700;font-size:20px;color:#a9a9a9;letter-spacing:1px}
.slider-dots{position:absolute;left:575px;top:551px;display:flex;gap:8px}
.slider-dots span{width:10px;height:10px;border-radius:50%;border:1px solid #bbb}
.slider-dots .on{background:#999;border-color:#999}

/* welcome */
.welcome{top:1298px;height:331px}
.band-bg{position:absolute;inset:0;background:linear-gradient(120deg,#1f4a87 0%,#1a3c70 55%,#163463 100%)}
.welcome-title{position:absolute;left:0;width:1200px;top:56px;text-align:center;font-family:"Rubik",sans-serif;font-weight:500;font-size:34px;color:var(--white)}
.welcome-text{position:absolute;left:340px;width:520px;top:118px;text-align:center;font-size:10.5px;line-height:21px;font-style:italic;color:#e2e9f4}

/* services */
.services{top:1629px;height:586px;background:var(--soft)}
.section-title{position:absolute;left:0;width:1200px;text-align:center;font-family:"Rubik",sans-serif;font-weight:500;font-size:32px;color:var(--ink)}
.section-title em{font-style:normal;color:var(--red)}
.service-card{position:absolute;top:127px;width:262px;height:391px;background:var(--white);box-shadow:0 1px 4px rgba(0,0,0,.07)}
.service-card.featured{background:linear-gradient(180deg,var(--orange) 0%,var(--red) 50%,#b92a1f 100%)}
.service-icon{position:absolute;left:83px;top:38px}
.service-name{position:absolute;left:0;width:262px;top:160px;text-align:center;font-family:"Rubik",sans-serif;font-size:14px;line-height:21px;color:var(--ink)}
.service-desc{position:absolute;left:22px;width:218px;top:210px;text-align:center;font-size:10px;line-height:19px;color:#8a8a8a}
.featured .service-name,.featured .service-desc{color:var(--white)}

/* intent & qa */
.intent{top:2215px;height:435px;background:var(--white)}
.qa{top:2650px;height:435px;background:var(--white)}
.prospora-mark{position:absolute;left:161px;top:125px;display:flex;align-items:center;gap:10px}
.prospora-square{width:18px;height:18px;background:var(--orange)}
.prospora-name{font-family:"Rubik",sans-serif;font-weight:400;font-size:30px;letter-spacing:4px;color:#2b2b2b}
.feature-title{position:absolute;font-family:"Rubik",sans-serif;font-weight:500;font-size:32px;color:var(--ink)}
.feature-text{position:absolute;width:500px;font-size:10px;line-height:19px;color:#8a8a8a}

/* feedback */
.feedback{top:3085px;height:450px}
.quote-frame{position:absolute;left:271px;top:174px;width:659px;height:191px;border:1px solid rgba(255,255,255,.55)}
.quote-badge{position:absolute;left:567px;top:140px;width:68px;height:68px;border-radius:50%;background:var(--red);display:flex;align-items:center;justify-content:center;font-family:"Rubik",sans-serif;font-size:52px;line-height:1;color:var(--white);padding-top:20px}
.quote-text{position:absolute;left:335px;width:530px;top:234px;text-align:center;font-size:11px;line-height:21px;font-style:italic;color:#e8eef7}
.client-pill{position:absolute;left:506px;top:350px;width:187px;height:30px;border-radius:15px;background:var(--white);display:flex;align-items:center;justify-content:center;font-family:"Rubik",sans-serif;font-size:12px;color:var(--ink)}
.slide-arrow{position:absolute;top:255px;width:28px;height:28px;background:var(--white);display:flex;align-items:center;justify-content:center}

/* contact */
.contact{top:3535px;height:450px;background:var(--white)}
.contact-sub{position:absolute;left:0;width:1200px;top:112px;text-align:center;font-size:11px;font-style:italic;color:#999}
.field{position:absolute;background:var(--soft);border:1px solid #ededed;font-size:10px;color:#777;padding:14px 12px}

/* footer */
.site-footer{top:3985px;height:375px;background:linear-gradient(180deg,#1d4683 0%,var(--navy-deep) 100%)}
.foot-head{position:absolute;top:60px;font-family:"Rubik",sans-serif;font-weight:500;font-size:14px;color:var(--white)}
.foot-text{position:absolute;font-size:10px;line-height:21px;color:#d5deec}
.foot-links{position:absolute;left:388px;top:94px;list-style:none;font-size:10px;line-height:21px;color:#d5deec}
.foot-brand{position:absolute;left:161px;top:96px;display:flex;align-items:center;gap:7px}
.foot-brand .brand-dot{width:24px;height:24px}
.foot-brand .brand-name{font-size:16px}
.social{position:absolute;left:161px;top:220px;display:flex;gap:8px}
.social span{width:32px;height:32px;border-radius:50%}
.touch-icon{position:absolute;left:609px;width:34px;height:34px;border-radius:50%;background:var(--red);display:flex;align-items:center;justify-content:center}
.subscribe{position:absolute;left:838px;top:176px;width:200px;height:38px;border-radius:19px;background:var(--white);font-size:10px;color:#777;padding:12px 16px}
.subscribe-btn{position:absolute;right:4px;top:4px;width:30px;height:30px;border-radius:50%;background:var(--red);display:flex;align-items:center;justify-content:center}
.copyright{position:absolute;left:0;width:1200px;top:338px;text-align:center;font-size:8.5px;color:#9fb1cc}
</style>
</head>
<body>
<div class="page">

<header class="hero">
  <svg class="hero-art" width="1200" height="730" viewBox="0 0 1200 730" aria-hidden="false">
    <defs>
      <linearGradient id="swoosh" x1="0" y1="1" x2="1" y2="0">
        <stop offset="0" stop-color="#e2531c"/>
        <stop offset="1" stop-color="#c9361d"/>
      </linearGradient>
      <linearGradient id="meeting" x1="0" y1="0" x2="1" y2="1">
        <stop offset="0" stop-color="#e9ecef"/>
        <stop offset="0.6" stop-color="#c7ccd3"/>
        <stop offset="1" stop-color="#8f98a6"/>
      </linearGradient>
    </defs>
    <path d="M1200,380 Q1090,570 780,668 Q1020,650 1200,530 Z" fill="url(#swoosh)"/>
    <path d="M655,625 L626,724 L725,660 Z" class="fill-red"/>
    <circle cx="755" cy="433" r="240" class="fill-red"/>
    <circle cx="755" cy="433" r="228" fill="url(#meeting)" role="img" aria-label="Photo of a business team meeting around a conference table"/>
  </svg>
  <div class="brand"><span class="brand-dot"></span><span class="brand-name">Ledgerwise Reach</span></div>
  <div class="brand-tag">The Demand Generation Company</div>
  <nav class="main-nav">
    <span class="active">Home</span><span>About</span><span>Our Services</span><span>Prospora &amp; QA Technology</span><span>Intent Data</span><span>Testimonials</span><span>Contact Us</span>
  </nav>
  <div class="search-btn"><svg width="16" height="16" viewBox="0 0 16 16"><circle cx="6.5" cy="6.5" r="5" fill="none" class="stroke-white" stroke-width="1.6"/><line x1="10.2" y1="10.2" x2="14.5" y2="14.5" class="stroke-white" stroke-width="1.8"/></svg></div>
  <h1 class="hero-title">LEDGERWISE<br>REACH</h1>
  <p class="hero-sub">The Demand Generation<br>Company</p>
  <a class="btn btn-red" style="left:161px;top:478px;width:120px;height:40px">LEARN MORE</a>
</header>

<section class="partners">
  <svg class="abs" style="left:280px;top:55px" width="320" height="360" viewBox="0 0 320 360">
    <defs>
      <linearGradient id="redDisc" x1="0" y1="0" x2="1" y2="1"><stop offset="0" stop-color="#e2531c"/><stop offset="1" stop-color="#b92a1f"/></linearGradient>
    </defs>
    <path d="M215,50 L250,7 L262,80 Z" fill="#d8421e"/>
    <circle cx="165" cy="189" r="153" fill="url(#redDisc)" role="img" aria-label="Photo of a smiling man sitting cross-legged with a laptop"/>
  </svg>
  <h2 class="who-title">Who we work with</h2>
  <div class="step-link" style="top:218px"></div>
  <div class="step-link" style="top:292px"></div>
  <div class="step" style="top:174px"><div class="step-num">1</div><div><div class="step-label">Downloads Per Month</div><div class="step-ticker">Ticker to 70,000+</div></div></div>
  <div class="step" style="top:248px"><div class="step-num">2</div><div><div class="step-label">Leads Delivered Per Month</div><div class="step-ticker">Ticker to 70,000+</div></div></div>
  <div class="step" style="top:323px"><div class="step-num">3</div><div><div class="step-label">Countries We Can Reach</div><div class="step-ticker">Ticker to 50+</div></div></div>
  <div class="client-row">
    <div class="client-box">QRT</div><div class="client-box">VKD</div><div class="client-box">Brindlow</div><div class="client-box">Kestrune</div><div class="client-box">Solvane</div><div class="client-box">Marrowell</div>
  </div>
  <div class="slider-dots"><span></span><span class="on"></span><span></span></div>
</section>

<section class="welcome">
  <div class="band-bg" role="img" aria-label="Navy-tinted photo of hands typing on a laptop beside a coffee cup"></div>
  <h2 class="welcome-title">Welcome To Ledgerwise Reach</h2>
  <p class="welcome-text">Ledgerwise Reach offers multi-channel demand generation services to publishers and technology vendors through our network of lead generation websites and native speaking telemarketing agents. Whether looking for MQL, ABM or BANT campaigns, Ledgerwise Reach can assist you in delivering your demand generation strategy and generate pipeline for your sales teams and/or channel partners.</p>
  <a class="btn btn-red" style="left:536px;top:228px;width:128px;height:40px">MORE ABOUT US</a>
</section>

<section class="services">
  <h2 class="section-title" style="top:56px">Our <em>Services</em></h2>

  <article class="service-card" style="left:161px">
    <svg class="service-icon" width="96" height="96" viewBox="0 0 96 96"><path d="M62,12 L80,4 L74,26 Z" class="fill-red"/><circle cx="48" cy="52" r="44" class="fill-red"/><rect x="30" y="34" width="26" height="22" rx="2" fill="none" class="stroke-white" stroke-width="2"/><line x1="34" y1="41" x2="52" y2="41" class="stroke-white" stroke-width="2"/><circle cx="58" cy="58" r="6" fill="none" class="stroke-white" stroke-width="2"/><path d="M48,74 Q58,62 68,74" fill="none" class="stroke-white" stroke-width="2"/></svg>
    <h3 class="service-name">Marketing Qualified<br>Leads (MQL)</h3>
    <p class="service-desc">A Marketing Qualified Lead (MQL) is a prospect that has expressed an interest in what your brand has to offer. An MQL has taken the first steps to becoming a customer and is ready to receive additional contact from your company.</p>
    <a class="btn btn-red" style="left:82px;top:325px;width:98px;height:32px;font-size:10px">LEARN MORE</a>
  </article>

  <article class="service-card featured" style="left:469px">
    <svg class="service-icon" width="96" height="96" viewBox="0 0 96 96"><path d="M62,12 L80,4 L74,26 Z" class="fill-white"/><circle cx="48" cy="52" r="44" class="fill-white"/><rect x="34" y="36" width="28" height="30" rx="3" fill="none" stroke="#1b3f76" stroke-width="2.5"/><circle cx="40" cy="44" r="4" class="fill-red"/><circle cx="56" cy="58" r="4" class="fill-red"/><line x1="40" y1="56" x2="50" y2="46" stroke="#1b3f76" stroke-width="2"/></svg>
    <h3 class="service-name">Account Based<br>Marketing Leads (ABM)</h3>
    <p class="service-desc">ABM is a strategy that directs marketing resources to engaging a specific set of target accounts. Instead of casting a wide net to engage any potential customers, marketers use ABM and work closely with sales.</p>
    <a class="btn btn-white" style="left:80px;top:325px;width:100px;height:32px;font-size:10px">LEARN MORE</a>
  </article>

  <article class="service-card" style="left:775px">
    <svg class="service-icon" width="96" height="96" viewBox="0 0 96 96"><path d="M62,12 L80,4 L74,26 Z" class="fill-red"/><circle cx="48" cy="52" r="44" class="fill-red"/><circle cx="56" cy="38" r="8" fill="none" class="stroke-white" stroke-width="2"/><path d="M28,64 L44,58 L62,62 L70,56" fill="none" class="stroke-white" stroke-width="2.2"/><line x1="32" y1="46" x2="32" y2="56" class="stroke-white" stroke-width="2"/><line x1="38" y1="42" x2="38" y2="56" class="stroke-white" stroke-width="2"/></svg>
    <h3 class="service-name">Sales Qualified Lead<br>/ BANT</h3>
    <p class="service-desc">An SQL lead or a BANT lead is a type of lead that has expressed a specific interest in a product and service that you have to offer ... The difference between marketing qualified leads (MQL) and sales qualified leads (SQL).</p>
    <a class="btn btn-red" style="left:80px;top:325px;width:100px;height:32px;font-size:10px">LEARN MORE</a>
  </article>
</section>

<section class="intent">
  <div class="prospora-mark"><span class="prospora-square"></span><span class="prospora-name">PROSPORA</span></div>
  <h2 class="feature-title" style="left:161px;top:190px">Intent Data</h2>
  <p class="feature-text" style="left:161px;top:243px">Our relationships with the world's most important technology &amp; business decisions makers generate a perpetual stream of global data. With access to 35 million individuals and a global behavioural data stream that is authenticated, timely and contextually relevant, we have one of the industry's most powerful signals of buyer intent and can fuel your demand-generation marketing strategies globally. We support our intent targeting capabilities by partnering with a number of third party intent providers.</p>
  <a class="btn btn-navy" style="left:161px;top:360px;width:120px;height:42px">LEARN MORE</a>
  <svg class="abs" style="left:725px;top:70px" width="330" height="340" viewBox="0 0 330 340">
    <defs><linearGradient id="redDisc2" x1="0" y1="0" x2="1" y2="1"><stop offset="0" stop-color="#b92a1f"/><stop offset="1" stop-color="#e2531c"/></linearGradient></defs>
    <path d="M80,40 L72,0 L120,30 Z" fill="#c2301f"/>
    <circle cx="160" cy="178" r="153" fill="url(#redDisc2)" role="img" aria-label="Photo of a businesswoman holding a newspaper and a coffee cup"/>
  </svg>
</section>

<section class="qa">
  <svg class="abs" style="left:155px;top:40px" width="320" height="330" viewBox="0 0 320 330">
    <defs>
      <linearGradient id="redDisc3" x1="0" y1="0" x2="1" y2="1"><stop offset="0" stop-color="#b92a1f"/><stop offset="1" stop-color="#e2531c"/></linearGradient>
      <linearGradient id="monitor" x1="0" y1="0" x2="0" y2="1"><stop offset="0" stop-color="#f4f5f7"/><stop offset="1" stop-color="#b8bcc3"/></linearGradient>
    </defs>
    <path d="M215,250 L245,320 L255,240 Z" fill="#c2301f"/>
    <circle cx="158" cy="154" r="150" fill="url(#redDisc3)"/>
  </svg>
  <div class="abs" role="img" aria-label="Illustration of a desktop monitor showing an email and telemarketing report" style="left:254px;top:67px;width:318px;height:263px;background:linear-gradient(180deg,#f4f5f7 0%,#d3d6db 75%,#aeb3ba 100%);border-radius:6px"></div>
  <h2 class="feature-title" style="left:665px;top:64px">QA Technology</h2>
  <p class="feature-text" style="left:665px;top:118px;width:375px">Prospora is a proprietary lead verification platform from Ledgerwise Reach that aims to sift out invalid leads with questionable or erroneous data. The platform is designed to equip sales teams with accurate, high-quality records in order to improve lead generation, accelerate pipeline and increase revenue.</p>
  <p class="feature-text" style="left:665px;top:208px;width:375px">Prospora is positioned to quickly identify, validate, and improve lead quality at the point-of-entry by filtering out all leads that do not match required filters, such as job title, company size, etc. The platform is designed to use real-time contact validation and live phone verification to remove all duplicate leads.</p>
  <a class="btn btn-navy" style="left:664px;top:309px;width:120px;height:42px">LEARN MORE</a>
</section>

<section class="feedback">
  <div class="band-bg" role="img" aria-label="Navy-tinted photo of colleagues working together at a desk"></div>
  <h2 class="section-title" style="top:56px;color:var(--white)">Client's Feedback</h2>
  <div class="quote-frame"></div>
  <div class="quote-badge">&ldquo;</div>
  <p class="quote-text">Lorem ipsum dolor sit amet, consectetur adipiscing elit, sed do eiusmod tempor incididunt ut labore et dolore magna aliqua. Ut enim ad minim veniam, quis nostrud exercitation ullamco laboris nisi ut aliquip ex ea commodo consequat. Duis aute irure dolor in reprehenderit in voluptate velit esse cillum dolore eu fugiat nulla pariatur. Excepteur sint occaecat cupidatat non proident.</p>
  <div class="client-pill">- Client's Name</div>
  <div class="slide-arrow" style="left:257px"><svg width="10" height="12" viewBox="0 0 10 12"><path d="M7,1 L2,6 L7,11" fill="none" stroke="#1d1d1d" stroke-width="1.6"/></svg></div>
  <div class="slide-arrow" style="left:916px"><svg width="10" height="12" viewBox="0 0 10 12"><path d="M3,1 L8,6 L3,11" fill="none" stroke="#1d1d1d" stroke-width="1.6"/></svg></div>
</section>

<section class="contact">
  <h2 class="section-title" style="top:56px">Contact Us</h2>
  <p class="contact-sub">Lorem ipsum dolor sit amet, consectetur adipiscing elit, sed do eiusmod tempor incididunt.</p>
  <div class="field" style="left:281px;top:166px;width:203px;height:44px">Name :</div>
  <div class="field" style="left:498px;top:166px;width:203px;height:44px">Email :</div>
  <div class="field" style="left:714px;top:166px;width:203px;height:44px">Phone :</div>
  <div class="field" style="left:281px;top:227px;width:636px;height:103px">Message / comments :</div>
  <a class="btn btn-navy" style="left:538px;top:347px;width:121px;height:40px">SUBMIT NOW</a>
</section>

<footer class="site-footer" role="contentinfo">
  <div class="abs" role="img" aria-label="Faint navy city skyline photo behind the footer" style="inset:0;background:linear-gradient(180deg,rgba(255,255,255,.04),rgba(0,0,0,.08))"></div>
  <h3 class="foot-head" style="left:161px">Contact Us</h3>
  <div class="foot-brand"><span class="brand-dot"></span><span class="brand-name">Ledgerwise Reach</span></div>
  <p class="foot-text" style="left:161px;top:150px;width:190px;font-style:italic">Lorem ipsum dolor sit amet, consectetur incididunt ut labore et dolore.</p>
  <div class="social"><span style="background:#4b6bb0"></span><span style="background:#2aa3e0"></span><span style="background:#1f7fc0"></span></div>

  <h3 class="foot-head" style="left:388px">Links</h3>
  <ul class="foot-links"><li>Home</li><li>About</li><li>Our services</li><li>Prospora &amp; QA Technology</li><li>Intent Data</li><li>Testimonials</li><li>Contact Us</li></ul>

  <h3 class="foot-head" style="left:613px">Get In Touch</h3>
  <div class="touch-icon" style="top:101px"><svg width="14" height="16" viewBox="0 0 14 16"><path d="M7,15 C3,10 1.5,8 1.5,5.5 A5.5,5.5 0 0 1 12.5,5.5 C12.5,8 11,10 7,15 Z" class="fill-white"/><circle cx="7" cy="5.5" r="2" class="fill-red"/></svg></div>
  <p class="foot-text" style="left:658px;top:92px">123,Address, State<br>Name, Street Name,City<br>Name, Zip Code</p>
  <div class="touch-icon" style="top:169px"><svg width="14" height="14" viewBox="0 0 14 14"><path d="M3,1 L5.5,1 L6.5,4 L5,5.2 C5.8,7 7,8.2 8.8,9 L10,7.5 L13,8.5 L13,11 C13,12.2 12,13 11,13 C5.5,12.5 1.5,8.5 1,3 C1,2 1.8,1 3,1 Z" class="fill-white"/></svg></div>
  <p class="foot-text" style="left:658px;top:176px">020 7946 0182</p>
  <div class="touch-icon" style="top:221px"><svg width="16" height="12" viewBox="0 0 16 12"><rect x="1" y="1" width="14" height="10" rx="1" fill="none" class="stroke-white" stroke-width="1.5"/><path d="M1.5,1.5 L8,7 L14.5,1.5" fill="none" class="stroke-white" stroke-width="1.5"/></svg></div>
  <p class="foot-text" style="left:658px;top:228px">info@ledgerwisereach.example</p>

  <h3 class="foot-head" style="left:838px">Stay Update</h3>
  <p class="foot-text" style="left:838px;top:94px;width:210px">Lorem ipsum dolor sit amet, consectetur adipiscing elit, sed do eiusmod tempor incididunt ut labore et dolore.</p>
  <div class="subscribe">Enter Email..<div class="subscribe-btn"><svg width="13" height="13" viewBox="0 0 13 13"><path d="M12,1 L1,5.5 L5.5,7.5 L7.5,12 Z" class="fill-white"/></svg></div></div>

  <p class="copyright">Copyright © ledgerwisereach 2020 . All Right Reserved.&nbsp;&nbsp; Privacy Policy&nbsp;&nbsp; Terms &amp; Conditions</p>
</footer>

</div>
</body>
</html>
```